Professional Corporate Business Card and Stationery Design for Freight Trucking Transportation Co.
Peter R. Malloy General Manager
Professional Corporate Business Card and Stationery Design for Freight Trucking Transportation Co. - Transportation
Creative Brief
Professional
Peter R. Malloy
V.P. of Operations / General Manager
7-48213 Upper Greyling Ridge Road Abbotsford, B.C. V2K4N7 Canada
HarrowTrans@pelvane.ca
This design project is for Business Cards and Business Stationey Harrow Transportation and Logistics Ltd. is a professional freight truck transport carrier based out of British Columbia, Canada. We provide highly crafted cargo delivery platforms to premier shippers of commodities throughout the five border Provinces of Canada and the Lower 48 United States of America. We are a "For-Hire" Motor Carrier which hauls shipper commodities from points within Canada to points within Canada and to points in the USA. We also transport freight from the United States into points within Canada. Threfore, we pride ourselves on superior performance and service, second to none in trucking freight industry. The above link will take you to what we feel is a example set of very highly crafted, upscale imagery designs created by artists on this very site and exemplifies the grit and character of true, quality Business card and Stationery designs, representation of the values of business professionalism we stand for and wish to convey in our stationery and other designs. Are you challenged enough to join in the fray and craft a unique design which can stand on par with those on this link? Today is April 25, 2014 - The challenge is to wow not only Harrow, but yourselves and your peers... ??
Harrow Harrow

```html
<!DOCTYPE html>
<html lang="en">
<head>
<meta charset="utf-8">
<title>Harrow Transportation and Logistics Ltd. — Business Card</title>
<link href="https://fonts.googleapis.com/css2?family=Questrial&display=swap" rel="stylesheet">
<style>
  :root {
    --backdrop: #4b4b4d;
    --card-dark: #231f20;
    --card-white: #ffffff;
    --panel-grey: #e4e4e6;
    --brand-red: #d71f26;
    --silver: #b9babd;
    --text-light: #f2f2f2;
  }
  html, body {
    margin: 0;
    width: 1200px;
    height: 895px;
    overflow: hidden;
    background: var(--backdrop);
    font-family: "Questrial", "Century Gothic", sans-serif;
  }
  .card {
    position: absolute;
    width: 560px;
    height: 320px;
    overflow: hidden;
    box-shadow: 0 6px 18px rgba(0,0,0,.35);
  }
  .card-shape { position: absolute; inset: 0; }
  .card--back { left: 150px; top: 100px; background: var(--card-dark); }
  .card--front { left: 490px; top: 470px; background: var(--card-white); }

  .brand {
    position: absolute;
    display: flex;
    flex-direction: column;
    align-items: center;
  }
  .brand-name {
    display: flex;
    align-items: center;
    gap: 7px;
    color: var(--brand-red);
    font-size: 26px;
    letter-spacing: 2px;
    line-height: 1;
  }
  .brand-dot {
    width: 14px; height: 14px;
    border-radius: 50%;
    background: var(--brand-red);
  }
  .brand-tagline {
    margin-top: 5px;
    color: var(--brand-red);
    font-size: 7px;
    letter-spacing: 1px;
  }
  .card--back .brand { left: 22px; top: 140px; }
  .card--front .brand { left: 0; right: 0; top: 58px; }

  .holder {
    position: absolute;
    right: 26px;
    top: 26px;
    text-align: right;
    color: var(--text-light);
  }
  .holder-name { font-size: 18px; letter-spacing: 1.5px; text-transform: uppercase; }
  .holder-title { font-size: 11px; margin-top: 3px; }
  .address {
    position: absolute;
    right: 26px;
    top: 118px;
    text-align: right;
    color: var(--text-light);
    font-size: 11px;
    line-height: 1.5;
  }
  .contact-list {
    position: absolute;
    right: 26px;
    top: 186px;
    margin: 0; padding: 0;
    list-style: none;
    color: var(--text-light);
    font-size: 9.5px;
  }
  .contact-list li {
    display: flex;
    justify-content: flex-end;
    align-items: center;
    gap: 8px;
    height: 21px;
  }
  .contact-icon { width: 11px; height: 11px; fill: var(--text-light); }

  .website {
    position: absolute;
    left: 0; right: 0;
    bottom: 30px;
    text-align: center;
    color: var(--card-white);
    font-size: 19px;
    letter-spacing: 5px;
  }
</style>
</head>
<body>

<section class="card card--back" aria-label="Business card, contact side">
  <svg class="card-shape" viewBox="0 0 560 320" preserveAspectRatio="none" aria-hidden="true">
    <defs>
      <radialGradient id="panelGlow" cx="0.3" cy="0.5" r="0.8">
        <stop offset="0" stop-color="#ffffff"/>
        <stop offset="1" stop-color="var(--panel-grey)"/>
      </radialGradient>
    </defs>
    <path d="M0 0 H170 C240 60 250 250 170 320 H0 Z" fill="var(--brand-red)"/>
    <path d="M0 0 H160 C228 60 236 250 160 320 H0 Z" fill="url(#panelGlow)"/>
  </svg>

  <div class="brand">
    <div class="brand-name"><span class="brand-dot"></span>HARROW</div>
    <div class="brand-tagline">TRANSPORT &amp; LOGISTICS</div>
  </div>

  <div class="holder">
    <div class="holder-name">Peter R. Malloy</div>
    <div class="holder-title">Managing Director</div>
  </div>

  <div class="address">41 Ninth Floor, Harbour<br>Line Road UK</div>

  <ul class="contact-list">
    <li>014 552 7310
      <svg class="contact-icon" viewBox="0 0 12 12" aria-hidden="true"><path d="M2.5 1 L4.5 1 L5.2 3.6 L4 4.6 C4.6 6 6 7.4 7.4 8 L8.4 6.8 L11 7.5 L11 9.5 C11 10.4 10.3 11 9.5 11 C5 10.7 1.3 7 1 2.5 C1 1.7 1.6 1 2.5 1 Z"/></svg>
    </li>
    <li>014 552 7311
      <svg class="contact-icon" viewBox="0 0 12 12" aria-hidden="true"><path d="M3.5 0.5 H8.5 A1 1 0 0 1 9.5 1.5 V10.5 A1 1 0 0 1 8.5 11.5 H3.5 A1 1 0 0 1 2.5 10.5 V1.5 A1 1 0 0 1 3.5 0.5 Z M3.7 2 V9 H8.3 V2 Z"/></svg>
    </li>
    <li>014 552 7312
      <svg class="contact-icon" viewBox="0 0 12 12" aria-hidden="true"><path d="M3 1 H8 V4 H3 Z M1 5 H11 V10 H1 Z"/></svg>
    </li>
    <li>peter@harrowfreight.ca
      <svg class="contact-icon" viewBox="0 0 12 12" aria-hidden="true"><path d="M1 2.5 H11 V9.5 H1 Z M1.6 3 L6 6.3 L10.4 3" stroke="var(--card-dark)" stroke-width="0.8"/></svg>
    </li>
    <li>www.harrowfreight.ca
      <svg class="contact-icon" viewBox="0 0 12 12" aria-hidden="true"><circle cx="6" cy="6" r="5.2"/><path d="M1 6 H11 M6 1 C3.8 3.5 3.8 8.5 6 11 M6 1 C8.2 3.5 8.2 8.5 6 11" stroke="var(--card-dark)" stroke-width="0.7" fill="none"/></svg>
    </li>
  </ul>
</section>

<section class="card card--front" aria-label="Business card, brand side">
  <svg class="card-shape" viewBox="0 0 560 320" preserveAspectRatio="none" aria-hidden="true">
    <defs>
      <linearGradient id="silverSweep" x1="0" x2="1" y1="0" y2="0">
        <stop offset="0" stop-color="#ffffff"/>
        <stop offset="0.5" stop-color="var(--silver)"/>
        <stop offset="1" stop-color="#ffffff"/>
      </linearGradient>
    </defs>
    <path d="M0 165 C150 225 410 225 560 165 V320 H0 Z" fill="url(#silverSweep)"/>
    <path d="M0 178 C150 238 410 238 560 178 V320 H0 Z" fill="var(--brand-red)"/>
  </svg>

  <div class="brand">
    <div class="brand-name"><span class="brand-dot"></span>HARROW</div>
    <div class="brand-tagline">TRANSPORT &amp; LOGISTICS</div>
  </div>

  <div class="website">www.harrowfreight.ca</div>
</section>

</body>
</html>
```